Dyrano In-home Personal Training

I would like to have some eye-catching business card design. Opened to any ideas.

The business idea: mobile fitness - train clients at their places

Target Market(s)

General population, 20-60 years old

Industry/Entity Type

Fitness

Contact Information for Business Card

The information to include:
Name: Marta
Call or text: 306-555-0187
Website: Dyrano.ca
Please use the attached logo

Requirements
Should not have
• No orange or purple colours please

```html
<!DOCTYPE html>
<html lang="en">
<head>
<meta charset="utf-8">
<title>Dyrano In-home Personal Training – Business Card</title>
<link href="https://fonts.googleapis.com/css2?family=Work+Sans:wght@300;400&display=swap" rel="stylesheet">
<style>
  :root {
    --page-bg: #262627;
    --card-dark: #48484b;
    --card-light: #ffffff;
    --ink-light: #ffffff;
    --ink-dark: #333335;
    --ink-muted: #444446;
  }
  * { box-sizing: border-box; margin: 0; padding: 0; }
  html, body {
    width: 1200px;
    height: 900px;
    overflow: hidden;
    background: var(--page-bg);
    font-family: "Work Sans", sans-serif;
  }
  .canvas {
    width: 1200px;
    height: 900px;
    display: flex;
    flex-direction: column;
    align-items: center;
    justify-content: center;
    gap: 40px;
  }
  .card {
    width: 700px;
    height: 400px;
    border-radius: 22px;
    position: relative;
    display: flex;
    flex-direction: column;
    align-items: center;
  }
  .card--back { background: var(--card-dark); color: var(--ink-light); justify-content: center; }
  .card--front { background: var(--card-light); color: var(--ink-dark); padding-top: 86px; }

  .brand { display: flex; flex-direction: column; align-items: flex-start; }
  .brand__row { display: flex; align-items: center; gap: 22px; }
  .brand__mark {
    width: 30px; height: 30px;
    border: 3px solid currentColor;
    border-radius: 50%;
  }
  .brand__name {
    font-weight: 300;
    font-size: 84px;
    letter-spacing: 14px;
    line-height: 1;
  }
  .brand__tagline {
    font-weight: 400;
    font-size: 14px;
    letter-spacing: 6px;
    margin-top: 6px;
    margin-left: 52px;
    text-transform: uppercase;
  }

  .details {
    display: flex;
    align-items: center;
    margin-top: 52px;
    gap: 38px;
  }
  .person { text-align: right; }
  .person__name { font-weight: 400; font-size: 46px; letter-spacing: 2px; line-height: 1; }
  .person__role { font-size: 17px; letter-spacing: 1px; margin-top: 6px; color: var(--ink-muted); }
  .divider { width: 2px; height: 84px; background: var(--ink-dark); }
  .contact { list-style: none; font-size: 23px; letter-spacing: 2px; }
  .contact__item { display: flex; align-items: center; gap: 12px; line-height: 1.45; }
  .contact__icon { width: 16px; height: 16px; flex: none; }
</style>
</head>
<body>
<main class="canvas">
  <section class="card card--back" aria-label="Card back">
    <div class="brand">
      <div class="brand__row">
        <span class="brand__mark"></span>
        <span class="brand__name">Dyrano</span>
      </div>
      <span class="brand__tagline">In-home personal training</span>
    </div>
  </section>

  <section class="card card--front" aria-label="Card front">
    <div class="brand">
      <div class="brand__row">
        <span class="brand__mark"></span>
        <span class="brand__name">Dyrano</span>
      </div>
      <span class="brand__tagline">In-home personal training</span>
    </div>
    <div class="details">
      <div class="person">
        <p class="person__name">Marta</p>
        <p class="person__role">Director</p>
      </div>
      <span class="divider"></span>
      <ul class="contact">
        <li class="contact__item">
          <svg class="contact__icon" viewBox="0 0 16 16" fill="none" stroke="currentColor" stroke-width="1.6" stroke-linejoin="round"><path d="M3 1.5h3l1 3.5-2 1.2c.8 1.8 2 3 3.8 3.8l1.2-2 3.5 1v3c0 .8-.7 1.5-1.5 1.5C6.8 13.5 2.5 9.2 1.5 3c0-.8.7-1.5 1.5-1.5z"/></svg>
          <span>306-555-0187</span>
        </li>
        <li class="contact__item">
          <svg class="contact__icon" viewBox="0 0 16 16" fill="none" stroke="currentColor" stroke-width="1.6" stroke-linejoin="round"><rect x="1" y="3" width="14" height="10" rx="1"/><path d="M1.5 3.5 8 9l6.5-5.5"/></svg>
          <span>Dyrano.ca</span>
        </li>
      </ul>
    </div>
  </section>
</main>
</body>
</html>
```